Willowbend Spine Chiropractic

office phone- 913-462-1037
After Hour number 913-284-6150
Office address 27814 Halvorn Rd. Overland Park Ks 66947
Dr. Marlon Pettigrew, DC
I added 3 different types of logos proofs.
Specalizing in:
Family Wellness Care
Auto Accident
Workman Comp Injuries
Urgent Alternative Pain Relief
Non-operative Sports Injury Care

```html
<!DOCTYPE html>
<html lang="en">
<head>
<meta charset="utf-8">
<title>Willowbend Spine Chiropractic – Business Card</title>
<link href="https://fonts.googleapis.com/css2?family=Lato:wght@400;700;900&display=swap" rel="stylesheet">
<style>
  :root {
    --navy: #242a7c;
    --red: #d21f2b;
    --ink: #1e1e28;
    --card: #f7f7f8;
    --backdrop: #2a2a2c;
    --emblem: #e6e6ea;
  }
  * { margin: 0; padding: 0; box-sizing: border-box; }
  html, body { width: 1200px; height: 997px; overflow: hidden; }
  body {
    background: var(--backdrop);
    font-family: "Lato", sans-serif;
    position: relative;
  }
  .card {
    position: absolute;
    left: 210px;
    width: 780px;
    height: 446px;
    background: var(--card);
    overflow: hidden;
    box-shadow: 0 12px 30px rgba(0,0,0,.5);
  }
  .card--front { top: 40px; }
  .card--back { top: 511px; }
  .card__bands { position: absolute; left: 0; bottom: 0; width: 780px; height: 60px; }
  .emblem {
    position: absolute;
    border-radius: 50%;
    background: radial-gradient(circle, var(--emblem) 0%, rgba(230,230,234,0) 70%);
  }
  .card--front .emblem { left: 180px; top: 20px; width: 320px; height: 320px; }
  .card--back .emblem { left: -60px; top: 60px; width: 300px; height: 300px; }

  .brand {
    position: absolute;
    display: flex;
    align-items: center;
    gap: 14px;
  }
  .brand__dot { border-radius: 50%; background: var(--red); flex: none; }
  .brand__name { color: var(--navy); font-weight: 900; white-space: nowrap; }
  .card--front .brand { left: 100px; top: 190px; }
  .card--front .brand__dot { width: 30px; height: 30px; }
  .card--front .brand__name { font-size: 40px; }
  .card--back .brand { left: 50px; top: 50px; }
  .card--back .brand__dot { width: 22px; height: 22px; }
  .card--back .brand__name { font-size: 30px; }

  .doctor { position: absolute; left: 50px; top: 140px; }
  .doctor__name { color: var(--navy); font-weight: 900; font-size: 24px; text-transform: uppercase; }
  .doctor__title { color: var(--ink); font-weight: 700; font-size: 15px; margin-top: 2px; }

  .contact { position: absolute; left: 50px; top: 245px; list-style: none; }
  .contact__item { display: flex; gap: 12px; color: var(--ink); font-weight: 700; font-size: 18px; line-height: 1.25; margin-bottom: 8px; }
  .contact__icon { width: 18px; height: 18px; flex: none; margin-top: 2px; }

  .divider {
    position: absolute; left: 392px; top: 140px; width: 3px; height: 170px;
    background: linear-gradient(to bottom, rgba(210,31,43,0), var(--red) 35%, var(--red) 60%, rgba(210,31,43,0));
  }
  .services { position: absolute; left: 425px; top: 140px; }
  .services__heading {
    color: var(--navy); font-weight: 900; font-size: 16px;
    text-decoration: underline; text-underline-offset: 3px; margin-bottom: 8px;
  }
  .services__list { list-style: none; }
  .services__item { color: var(--ink); font-weight: 700; font-size: 17px; line-height: 1.55; display: flex; align-items: center; gap: 8px; }
  .services__item::before { content: ""; width: 5px; height: 5px; border-radius: 50%; background: var(--navy); }
</style>
</head>
<body>
  <section class="card card--front" aria-label="Card front">
    <div class="emblem" role="img" aria-label="Faint practice emblem watermark"></div>
    <div class="brand">
      <span class="brand__dot"></span>
      <span class="brand__name">Willowbend Spine Chiropractic</span>
    </div>
    <svg class="card__bands" viewBox="0 0 780 60" aria-hidden="true">
      <path d="M0 46 H520 Q540 46 550 36 L556 30 Q560 26 568 26 H780 V60 H0 Z" fill="var(--red)"/>
      <path d="M0 46 H510 Q530 46 540 52 L552 60 H0 Z" fill="var(--navy)"/>
    </svg>
  </section>

  <section class="card card--back" aria-label="Card back">
    <div class="emblem" role="img" aria-label="Faint practice emblem watermark"></div>
    <div class="brand">
      <span class="brand__dot"></span>
      <span class="brand__name">Willowbend Spine Chiropractic</span>
    </div>

    <div class="doctor">
      <p class="doctor__name">Dr. Marlon Pettigrew</p>
      <p class="doctor__title">Doctor Of Chiropractic</p>
    </div>

    <ul class="contact">
      <li class="contact__item">
        <svg class="contact__icon" viewBox="0 0 24 24" aria-hidden="true"><path fill="var(--red)" d="M6.6 10.8a15.1 15.1 0 0 0 6.6 6.6l2.2-2.2c.3-.3.7-.4 1-.2 1.1.4 2.3.6 3.6.6.6 0 1 .4 1 1V20c0 .6-.4 1-1 1A17 17 0 0 1 3 4c0-.6.4-1 1-1h3.5c.6 0 1 .4 1 1 0 1.3.2 2.5.6 3.6.1.3 0 .7-.2 1z"/></svg>
        <span>913-462-1037</span>
      </li>
      <li class="contact__item">
        <svg class="contact__icon" viewBox="0 0 24 24" aria-hidden="true"><path fill="var(--red)" d="M12 2a7 7 0 0 0-7 7c0 5.2 7 13 7 13s7-7.8 7-13a7 7 0 0 0-7-7zm0 9.5A2.5 2.5 0 1 1 12 6.5a2.5 2.5 0 0 1 0 5z"/></svg>
        <span>27814 Halvorn Rd.<br>Overland Park Ks 66947</span>
      </li>
    </ul>

    <div class="divider"></div>

    <div class="services">
      <p class="services__heading">SPECIALIZING IN:</p>
      <ul class="services__list">
        <li class="services__item">Family Wellness Care</li>
        <li class="services__item">Auto Accident</li>
        <li class="services__item">Workman Comp Injuries</li>
        <li class="services__item">Urgent Alternative Pain Relief</li>
        <li class="services__item">Non-operative Sports Injury Care</li>
      </ul>
    </div>

    <svg class="card__bands" viewBox="0 0 780 60" aria-hidden="true">
      <path d="M0 46 H520 Q540 46 550 36 L556 30 Q560 26 568 26 H780 V60 H0 Z" fill="var(--red)"/>
      <path d="M0 46 H510 Q530 46 540 52 L552 60 H0 Z" fill="var(--navy)"/>
    </svg>
  </section>
</body>
</html>
```